Redesign current business card for food company

i would like to redesign my business card. our company is food company, our product range from chips, juices, milk and etc (mostly dried food stuff).
I want o keep same logo but , the rest is open to new design.
you can check at our website about our company www.torvikeats.com

Target Market(s)

most of food company

Industry/Entity Type

Business

Contact Information for Business Card

I want to keep more to blue color...

Colors
3176b5
abd036

Requirements
Must have
• our old logo
Nice to have
• we do not mind to have nice material on bus card in order to accomplish nice design. for example: using spot uv, embossed and etc.

```html
<!DOCTYPE html>
<html lang="en">
<head>
<meta charset="utf-8">
<title>Torvik Business Card</title>
<link rel="stylesheet" href="https://fonts.googleapis.com/css2?family=Lato:ital,wght@0,400;0,700;1,400&display=swap">
<style>
  :root {
    --backdrop: #2b2b2b;
    --paper: #ffffff;
    --brand-blue: #1c36ad;
    --deep-blue: #1a2ab0;
    --bright-cyan: #0aa6cc;
    --leaf-green: #14b43a;
    --ink-light: #ffffff;
  }
  * { box-sizing: border-box; margin: 0; padding: 0; }
  html, body { width: 1200px; height: 987px; overflow: hidden; }
  body {
    background: var(--backdrop);
    font-family: "Lato", sans-serif;
    position: relative;
  }
  .card {
    position: absolute;
    left: 293px;
    width: 615px;
    height: 352px;
    overflow: hidden;
  }
  .card--front { top: 130px; background: var(--paper); }
  .card--back {
    top: 505px;
    background: radial-gradient(ellipse 60% 75% at 50% 50%, var(--bright-cyan) 0%, #0b74c4 45%, var(--deep-blue) 100%);
  }
  .front-art { position: absolute; inset: 0; width: 100%; height: 100%; }
  .wordmark {
    position: absolute;
    left: 40px;
    top: 38px;
    font-size: 78px;
    font-weight: 700;
    color: var(--brand-blue);
    letter-spacing: -1px;
    line-height: 1;
  }
  .holder {
    position: absolute;
    right: 27px;
    top: 66px;
    text-align: right;
  }
  .holder__name { font-size: 20px; font-weight: 700; color: var(--brand-blue); line-height: 24px; }
  .holder__title { font-size: 15px; color: var(--leaf-green); line-height: 20px; }
  .contacts {
    position: absolute;
    right: 26px;
    top: 205px;
    list-style: none;
    color: var(--ink-light);
    font-size: 15px;
  }
  .contacts li {
    display: flex;
    justify-content: flex-end;
    align-items: center;
    height: 23.5px;
  }
  .contacts svg { width: 16px; height: 16px; margin-left: 10px; fill: var(--ink-light); }
  .address {
    position: absolute;
    right: 26px;
    top: 310px;
    color: var(--ink-light);
    font-size: 15px;
  }
  .back-name {
    position: absolute;
    left: 0; right: 0;
    top: 140px;
    text-align: center;
    font-size: 44px;
    font-weight: 700;
    color: var(--ink-light);
    line-height: 1;
  }
  .website {
    position: absolute;
    left: 0; right: 0;
    top: 284px;
    text-align: center;
    font-size: 16px;
    font-style: italic;
    letter-spacing: 3px;
    color: var(--ink-light);
  }
</style>
</head>
<body>
  <section class="card card--front">
    <svg class="front-art" viewBox="0 0 525 300" preserveAspectRatio="none" aria-hidden="true">
      <defs>
        <radialGradient id="swoosh-blue" cx="330" cy="225" r="260" gradientUnits="userSpaceOnUse">
          <stop offset="0" stop-color="#0aa6cc"/>
          <stop offset="0.5" stop-color="#0b6fc4"/>
          <stop offset="1" stop-color="#1a2ab0"/>
        </radialGradient>
      </defs>
      <path class="swoosh-green" d="M0 300 L0 283 Q240 150 525 134 L525 140 Q250 158 45 300 Z" fill="#14b43a"/>
      <path class="swoosh-blue" d="M46 300 Q252 162 525 140 L525 300 Z" fill="url(#swoosh-blue)" stroke="#ffffff" stroke-width="1.4"/>
    </svg>

    <div class="wordmark">torvik</div>

    <div class="holder">
      <p class="holder__name">Marcus Hallendra</p>
      <p class="holder__title">President</p>
    </div>

    <ul class="contacts">
      <li>555 214 3080
        <svg viewBox="0 0 16 16"><path d="M3 1.5 L6 1 L7.5 5 L5.5 6.5 Q7 9.5 9.5 10.5 L11 8.5 L15 10 L14.5 13 Q13 15 10 14 Q3 11 1.5 5 Q1.5 2.5 3 1.5 Z"/></svg>
      </li>
      <li>555 372 9146
        <svg viewBox="0 0 16 16"><path d="M4 0.5 H12 V15.5 H4 Z M5.5 2.5 V12 H10.5 V2.5 Z M7 13 H9 V14.3 H7 Z" fill-rule="evenodd"/></svg>
      </li>
      <li>555 214 3071
        <svg viewBox="0 0 16 16"><path d="M4 1 H12 V5 H4 Z M1 6 H15 V12 H12 V10 H4 V12 H1 Z M4.5 11 H11.5 V15 H4.5 Z"/></svg>
      </li>
      <li>marcus@torvikeats.com
        <svg viewBox="0 0 16 16"><path d="M1 3.5 H15 V12.5 H1 Z M2 4.5 L8 9 L14 4.5" fill="none" stroke="#ffffff" stroke-width="1.3"/></svg>
      </li>
    </ul>

    <p class="address">2418 Alder Row, Fairhaven CA 90412</p>
  </section>

  <section class="card card--back">
    <p class="back-name">torvik</p>
    <p class="website">www.torvikeats.com</p>
  </section>
</body>
</html>
```